Simplified minimalist but bold website

Design a website for a brand 'Brighten Each Morning' that shares ideas to make managing home and health easier through email swap series, webinars and eventually courses.

Simple landing page to attract users to sign up for a freebie.

Target Market(s)

women with families & homes to run

Number of Pages Required

1 page

Font styles to use
Sans Serif

Colors
e667a6
b768aa
acd136
ffffff
959595

Requirements
Must have
• Simplified look, line icons, opt-in template, contact us form

```html
<!DOCTYPE html>
<html lang="en">
<head>
<meta charset="utf-8">
<title>Brighten Each Morning</title>
<link href="https://fonts.googleapis.com/css2?family=Open+Sans:wght@300;400;600;700&display=swap" rel="stylesheet">
<style>
:root{
  --pink:#e667a6;
  --purple:#b768aa;
  --green:#acd136;
  --blue:#3a9ad9;
  --white:#ffffff;
  --grey:#959595;
  --ink:#444444;
  --panel:#efefef;
  --panel-dark:#e4e4e4;
  --footer:#e9e9e9;
}
*{box-sizing:border-box;margin:0;padding:0}
html,body{width:1200px;height:2316px;overflow:hidden}
body{font-family:"Open Sans",Arial,sans-serif;color:var(--ink);background:var(--white);position:relative}

.hero{position:absolute;left:0;top:0;width:1200px;height:580px;
  background:linear-gradient(180deg,#1f4f95 0%,#3f7cc0 32%,#a9c8e6 55%,#6f99c0 62%,#3b6f8e 72%,#486f5a 100%);
  text-align:center;color:var(--white)}
.hero-title{position:absolute;top:68px;left:0;width:100%;font-size:46px;font-weight:700}
.hero-rule{position:absolute;top:150px;left:575px;width:50px;height:3px;background:var(--white)}
.hero-lead{position:absolute;top:222px;left:0;width:100%;font-size:33px;font-weight:300;line-height:44px}
.hero-lead strong{font-weight:700}

.choices{position:absolute;top:580px;left:0;width:1200px;height:740px;display:flex;background:var(--panel)}
.divider{position:absolute;left:599px;top:0;width:2px;height:740px;background:var(--white)}
.or-badge{position:absolute;left:580px;top:-20px;width:40px;height:40px;border-radius:50%;background:var(--white);border:2px solid var(--panel-dark);
  font-size:14px;font-weight:600;color:var(--grey);text-align:center;line-height:36px}
.offer{width:600px;height:740px;position:relative;text-align:center}
.offer-kicker{position:absolute;top:20px;left:0;width:100%;font-size:17px;color:var(--grey);letter-spacing:1px}
.offer-title{position:absolute;top:82px;left:0;width:100%;font-size:30px;font-weight:700}
.offer-title.swaps{color:var(--purple)}
.offer-title.guide{color:var(--pink)}
.offer-rule{position:absolute;top:138px;left:280px;width:40px;height:3px}
.swaps-rule{background:var(--purple)}
.guide-rule{background:var(--pink)}
.offer-tagline{position:absolute;top:200px;left:0;width:100%;font-size:18px;font-weight:600}
.offer-text{position:absolute;top:240px;left:130px;width:340px;font-size:14px;line-height:22px;color:var(--grey)}
.offer-buttons{position:absolute;top:352px;left:130px;width:340px;display:flex;justify-content:space-between}
.pill{width:160px;height:38px;font-size:12px;font-weight:700;color:var(--white);line-height:38px;border-radius:3px;letter-spacing:.5px}
.pill.green{background:var(--green)}
.pill.blue{background:var(--blue)}
.offer-ask{position:absolute;top:440px;left:0;width:100%;font-size:18px;font-weight:600}
.guide-art{position:absolute;top:190px;left:180px;width:240px;height:220px;border-radius:6px;
  background:linear-gradient(135deg,#fafafa 0%,#e6e6e6 100%)}
.field{position:absolute;left:130px;width:340px;height:40px;background:var(--white);border:1px solid #dddddd;border-radius:3px;
  font-size:14px;color:var(--grey);text-align:left;padding-left:40px;line-height:38px}
.field svg{position:absolute;left:14px;top:12px}
.field.email{top:494px}
.field.name{top:554px}
.submit{position:absolute;top:612px;left:130px;width:340px;height:46px;background:var(--purple);color:var(--white);
  font-size:16px;font-weight:700;line-height:46px;border-radius:3px;letter-spacing:.5px}

.details{position:absolute;top:1320px;left:0;width:1200px;height:670px;text-align:center}
.details-title{position:absolute;top:60px;left:0;width:100%;font-size:36px;font-weight:400;color:var(--ink)}
.details-rule{position:absolute;top:126px;left:580px;width:40px;height:3px;background:var(--ink)}
.details-text{position:absolute;left:350px;width:500px;font-size:15px;line-height:22px;color:var(--ink)}
.details-text.p1{top:188px}
.details-text.p2{top:300px}
.details-text.p3{top:380px}
.details-cta{position:absolute;top:470px;left:495px;width:210px;height:50px;background:var(--purple);color:var(--white);
  font-size:17px;font-weight:700;line-height:50px;border-radius:3px}

.footer{position:absolute;top:1990px;left:0;width:1200px;height:270px;background:var(--footer)}
.brand{position:absolute;top:80px;left:140px;font-size:40px;font-weight:600;color:var(--purple)}
.foot-col{position:absolute;top:60px}
.foot-col.contact{left:630px}
.foot-col.social{left:940px}
.foot-head{font-size:14px;font-weight:700;margin-bottom:20px;letter-spacing:.5px}
.foot-item{display:flex;align-items:flex-start;font-size:13px;color:#666;margin-bottom:16px;line-height:18px}
.foot-item svg{flex:none;margin-right:12px;margin-top:1px}
.dot{width:24px;height:24px;border-radius:50%;flex:none;margin-right:12px;margin-top:-3px}
.dot.a{background:#3b5a98}.dot.b{background:#38a1f3}.dot.c{background:#0e76a8}
.copyright{position:absolute;top:2260px;left:0;width:1200px;height:56px;text-align:center;font-size:13px;color:#666;line-height:56px}
</style>
</head>
<body>

<header class="hero" role="img" aria-label="Photo of a person with arms raised on a pier over a calm lake under a blue sky">
  <h1 class="hero-title">Brighten Each Morning.</h1>
  <div class="hero-rule"></div>
  <p class="hero-lead">Chances are life is a little<br>overwhelming. <strong>Let us help</strong></p>
</header>

<section class="choices">
  <div class="offer">
    <p class="offer-kicker">Baby Steps... (try out a few of our tricks)</p>
    <h2 class="offer-title swaps">Swaps Email Series</h2>
    <div class="offer-rule swaps-rule"></div>
    <p class="offer-tagline">Save TIME, MONEY and SANITY with simple product swaps.</p>
    <p class="offer-text">Reduce the amount of work it takes to run your home. Swap out existing products for more sustainable ones. Each swap saves you work, clutter, time &amp; money.</p>
    <div class="offer-buttons">
      <div class="pill green">SEE SAMPLE SWAP</div>
      <div class="pill blue">LEARN MORE</div>
    </div>
    <p class="offer-ask">Send your ideas my way...</p>
    <div class="field email"><svg width="16" height="14" viewBox="0 0 16 14"><rect x="1" y="2" width="14" height="10" fill="none" stroke="#959595" stroke-width="1.5"/><path d="M1 2l7 6 7-6" fill="none" stroke="#959595" stroke-width="1.5"/></svg>Email</div>
    <div class="field name"><svg width="16" height="14" viewBox="0 0 16 14"><circle cx="8" cy="4" r="3" fill="#959595"/><path d="M2 14c0-4 3-6 6-6s6 2 6 6z" fill="#959595"/></svg>Name</div>
    <div class="submit">SEND ME THE GUIDE!</div>
  </div>

  <div class="offer">
    <p class="offer-kicker">Big Leap... (I'm ready to roll up my sleeves)</p>
    <h2 class="offer-title guide">Decluttering Guide</h2>
    <div class="offer-rule guide-rule"></div>
    <div class="guide-art" role="img" aria-label="Illustration of two pinned paper notes reading steps and simple"></div>
    <div class="field email"><svg width="16" height="14" viewBox="0 0 16 14"><rect x="1" y="2" width="14" height="10" fill="none" stroke="#959595" stroke-width="1.5"/><path d="M1 2l7 6 7-6" fill="none" stroke="#959595" stroke-width="1.5"/></svg>Email</div>
    <div class="field name"><svg width="16" height="14" viewBox="0 0 16 14"><circle cx="8" cy="4" r="3" fill="#959595"/><path d="M2 14c0-4 3-6 6-6s6 2 6 6z" fill="#959595"/></svg>Name</div>
    <div class="submit">SIGN ME UP!</div>
  </div>

  <div class="divider"></div>
  <div class="or-badge">or</div>
</section>

<section class="details">
  <h2 class="details-title">Swaps Email Series</h2>
  <div class="details-rule"></div>
  <p class="details-text p1">Save TIME, MONEY and SANITY with simple product swaps. Greatly reduce the amount of work it takes to run your home. Swap out existing products for more sustainable ones. Each swap saves you work, clutter, time &amp; money.</p>
  <p class="details-text p2">You get an email 2x weekly for 6-12 weeks only. Get even more if you find they are helpful to you.</p>
  <p class="details-text p3">Join our monthly SIMPLE SWAP SHARING with other moms and get even more ideas. Better yet, come with great tips of your own to share.</p>
  <div class="details-cta">SIGN ME UP!</div>
</section>

<footer class="footer">
  <div class="brand">Brighten Each Morning</div>
  <div class="foot-col contact">
    <p class="foot-head">CONTACT US</p>
    <div class="foot-item"><svg width="12" height="16" viewBox="0 0 12 16"><path d="M6 0a6 6 0 0 0-6 6c0 4 6 10 6 10s6-6 6-10a6 6 0 0 0-6-6zm0 8.5A2.5 2.5 0 1 1 6 3.5a2.5 2.5 0 0 1 0 5z" fill="#666"/></svg>123 Maple Lane<br>Springfield, ST 40510</div>
    <div class="foot-item"><svg width="14" height="14" viewBox="0 0 14 14"><path d="M3 0l3 3-2 2c1 2 3 4 5 5l2-2 3 3-2 3C6 14 0 8 0 3z" fill="#666"/></svg>555-0142</div>
    <div class="foot-item"><svg width="14" height="12" viewBox="0 0 14 12"><rect x="0" y="0" width="14" height="12" fill="#666"/><path d="M0 0l7 6 7-6" fill="none" stroke="#e9e9e9" stroke-width="1.5"/></svg>hello@brighteneachmorning.com</div>
  </div>
  <div class="foot-col social">
    <p class="foot-head">CONNECT WITH US</p>
    <div class="foot-item"><span class="dot a"></span>Fambook</div>
    <div class="foot-item"><span class="dot b"></span>Chirper</div>
    <div class="foot-item"><span class="dot c"></span>WorkLink</div>
  </div>
</footer>
<div class="copyright">Copyright © 2016 All Rights Reserved</div>

</body>
</html>
```